facial aesthetics advertising dermal fillers for lip and facial rejuvenation

the poster(s) is to engage the interest of patients in a dental surgery. I am introducing new service and wish to attract interest and increase bookings. the service is facial rejuvenation using dermal fillers to reinstore youthfulness vitality and lost volume to the ageing female and male patients as well as to volumise lips in those patients who want fuller lips. upon seeing the poster the patient should feel positive
Updates

Project Deadline Extended
Reason: Looking for a client-pulling stand out design which communicates effectively the service of facial rejuvenation, restoration of vitality and returning patients their self-confidence. Graphics need to be of realistic men and women who are aged mid 30 onwards. Images should also include before and after treatments. These images can be sent over if required. Please see original brief for other details Many thanks for reading through and helping the cause.

Target Market(s)

18-65+

Industry/Entity Type

Dental

Colors

Designer to choose colors to be used in the design.

Requirements
Must have
• 1.clear images of female at forefront (perhaps male in the background looking happily at the woman) attractive features
• full lips
• age perhaps mid 30s
• 2. pre and post dermal filler treatment poster.
Nice to have
• eye catching but not brash
• sophisticated and positive

```html
<!DOCTYPE html>
<html lang="en">
<head>
<meta charset="UTF-8">
<title>Pre and Post Dermal Filler Treatment</title>
<link href="https://fonts.googleapis.com/css2?family=Ubuntu:wght@500;700&family=Lato:wght@400;700;900&display=swap" rel="stylesheet">
<style>
  :root {
    --teal: #138a7b;
    --mint: #cfe9e4;
    --mint-light: #e4f4f1;
    --charcoal: #3a3a3a;
    --band: #3d3d3d;
    --white: #ffffff;
    --stage: #eeeeee;
  }
  * { margin: 0; padding: 0; box-sizing: border-box; }
  html, body { width: 1200px; height: 900px; overflow: hidden; }
  body { background: var(--stage); font-family: "Lato", sans-serif; }
  .poster {
    position: absolute; left: 375px; top: 0;
    width: 450px; height: 900px; overflow: hidden;
    background: linear-gradient(160deg, var(--mint-light) 0%, var(--mint) 45%, var(--mint-light) 70%, var(--mint) 100%);
  }
  .poster__art { position: absolute; inset: 0; }
  .headline text { font-family: "Ubuntu", sans-serif; font-weight: 700; }
  .headline .teal { fill: var(--teal); }
  .headline .dark { fill: var(--charcoal); }
  .headline .light { font-weight: 500; }
  .result-label { font-family: "Lato", sans-serif; font-size: 5px; font-weight: 700; fill: #555; }
  .services {
    position: absolute; left: 0; top: 514px; width: 450px; height: 68px;
    background: var(--band); color: var(--white);
    display: flex; flex-direction: column; justify-content: center; align-items: center;
    font-family: "Lato", sans-serif; font-weight: 700; font-size: 25px; line-height: 1.1;
    text-transform: uppercase; letter-spacing: 0.2px;
  }
  .contact {
    position: absolute; left: 16px; top: 806px;
    color: var(--charcoal); font-family: "Lato", sans-serif; font-style: normal;
    font-size: 17.5px; line-height: 1.0;
  }
  .website {
    position: absolute; left: 0; bottom: 0; width: 450px; height: 36px;
    background: var(--teal); color: var(--white);
    display: flex; align-items: center; justify-content: center;
    font-family: "Lato", sans-serif; font-weight: 900; font-size: 17px; letter-spacing: 3.2px;
  }
</style>
</head>
<body>
<main class="poster">
  <svg class="poster__art" width="450" height="900" viewBox="0 0 450 900">
    <defs>
      <linearGradient id="portraitTone" x1="0" y1="0" x2="0.3" y2="1">
        <stop offset="0" stop-color="#f4f1ee"/>
        <stop offset="0.45" stop-color="#e8cfc1"/>
        <stop offset="1" stop-color="#dcb8a4"/>
      </linearGradient>
      <linearGradient id="faceTone" x1="0" y1="0" x2="0" y2="1">
        <stop offset="0" stop-color="#e6d3a8"/>
        <stop offset="0.45" stop-color="#e9c9b2"/>
        <stop offset="1" stop-color="#f3e6dc"/>
      </linearGradient>
      <linearGradient id="sweep" x1="0" y1="0" x2="1" y2="1">
        <stop offset="0" stop-color="#ffffff" stop-opacity="0.35"/>
        <stop offset="1" stop-color="#ffffff" stop-opacity="0"/>
      </linearGradient>
    </defs>

    <path class="bg-sweep" d="M0 300 C 120 420, 260 520, 450 560 L 450 640 C 260 600, 100 500, 0 400 Z" fill="url(#sweep)"/>
    <path class="bg-sweep" d="M0 640 C 120 700, 260 820, 450 840 L 450 870 C 240 860, 100 760, 0 700 Z" fill="url(#sweep)"/>

    <path class="portrait" role="img" aria-label="Portrait photo of a woman with full red lips and sleek dark hair"
          d="M228 0 C 168 80, 150 200, 210 268 C 262 326, 362 330, 410 390 C 432 412, 446 432, 450 456 L 450 0 Z"
          fill="url(#portraitTone)"/>
    <path class="portrait-frame" d="M228 0 C 168 80, 150 200, 210 268 C 262 326, 362 330, 410 390 C 432 412, 446 432, 450 456"
          fill="none" stroke="var(--teal)" stroke-width="8"/>

    <g class="headline">
      <text class="teal" x="12" y="252" font-size="92" textLength="148" lengthAdjust="spacingAndGlyphs">pre</text>
      <text class="dark light" x="68" y="296" font-size="62" textLength="104" lengthAdjust="spacingAndGlyphs">and</text>
      <text class="teal" x="16" y="352" font-size="92" textLength="200" lengthAdjust="spacingAndGlyphs">post</text>
      <text class="dark" x="100" y="418" font-size="84" textLength="252" lengthAdjust="spacingAndGlyphs">dermal</text>
      <text class="dark" x="10" y="466" font-size="84" textLength="166" lengthAdjust="spacingAndGlyphs">filler</text>
      <text class="teal light" x="189" y="466" font-size="56" textLength="245" lengthAdjust="spacingAndGlyphs">treatment</text>
    </g>

    <g class="results">
      <ellipse cx="300" cy="714" rx="236" ry="106" fill="var(--white)" stroke="var(--teal)" stroke-width="7"/>
      <rect class="result-photo" role="img" aria-label="Before treatment photo of a woman with short blonde hair"
            x="138" y="636" width="100" height="148" rx="40" fill="url(#faceTone)"/>
      <rect class="result-photo" role="img" aria-label="After treatment photo of the same woman with smoother skin"
            x="332" y="636" width="100" height="148" rx="40" fill="url(#faceTone)"/>
      <text class="result-label" x="188" y="794" text-anchor="middle">BEFORE</text>
      <text class="result-label" x="382" y="794" text-anchor="middle">AFTER</text>
    </g>
  </svg>

  <div class="services">
    <span>Anti Wrinkle Injections</span>
    <span>Dermal Fillers</span>
  </div>

  <address class="contact">
    555 014 2280<br>
    Your Address here<br>
    youemail@here.com
  </address>

  <div class="website">www.yourwebsitehere.com</div>
</main>
</body>
</html>
```